Victorian Era general store concept

I want to design a Victorian era general store themed web site. I Have existing advertisements from the Harrowgate Courier from the 1850's that display the Trumbo and Kessler brand. I would like to create a logo with that and if the designer can add any anything to it that would enhance the look yet retain its classic Victorian appear that would be great. I will upload the Harrowgate courier publication. Look for Trumbo and Kessler ads on there. I would like the design to be simplistic yet classic. Nothing to busy. I would like to add the phrase "A puget sound orginal" "Est. 1851"
https://www.archivexa.example/library/papers/papers_detail.aspx?t=29
Updates

I am going to upload another file that is very clear. Trumbo and Kessler regular line of packets. Hopefully this will help.

Target Market(s)

Undetermined

Industry/Entity Type

Online Store

Number of Pages Required

1 page

Font styles to use
Other font styles liked:
• What is on the adds.

Colors

Designer to choose colors to be used in the design.

Requirements
Must have
• Puget Sound orginal and est 1851
• Any "Trumbo and Kessler" advertisement from the Harrowgate Courier with details thereof.
Nice to have
• Some type of ship in the logo would be nice if it fits well.

```html
<!DOCTYPE html>
<html lang="en">
<head>
<meta charset="utf-8">
<title>Trumbo and Kessler</title>
<link href="https://fonts.googleapis.com/css2?family=Playfair+Display:ital,wght@0,400;0,700;1,400&family=Open+Sans:wght@400&display=swap" rel="stylesheet">
<style>
:root{
  --paper:#fcfbf6;
  --ink:#444444;
  --ink-soft:#555555;
  --bar:#4a4a4a;
  --bar-text:#f2f2f2;
  --rule:#5a4a48;
  --white:#ffffff;
}
*{box-sizing:border-box;margin:0;padding:0}
html,body{width:814px;height:1200px;overflow:hidden;background:var(--paper)}
body{position:relative;font-family:"Playfair Display",Georgia,serif;color:var(--ink)}
a{color:inherit}

.topbar{position:absolute;left:0;top:0;width:814px;height:25px;background:var(--bar);color:var(--bar-text);font:400 9px/25px "Open Sans",Arial,sans-serif}
.topbar .nav{position:absolute;left:59px;display:flex;gap:11px}
.topbar .contact{position:absolute;right:64px;display:flex;gap:34px;align-items:center}
.topbar .contact span{display:flex;align-items:center;gap:5px}
.topbar svg{width:8px;height:8px;fill:var(--bar-text)}

.masthead{position:absolute;left:59px;top:25px;width:695px;text-align:center}
.brand{margin-top:16px;font:700 28px/1 "Playfair Display",Georgia,serif;letter-spacing:1px;color:var(--ink)}
.masthead .rule-top{margin-top:18px;border-top:1px solid var(--ink-soft)}
.tagline{margin-top:12px;font:italic 400 11px/1 "Playfair Display",Georgia,serif;color:var(--ink)}
.masthead .rule-double{margin-top:11px;height:4px;border-top:1px solid var(--rule);border-bottom:1px solid var(--rule)}

.block{position:absolute}
.photo{display:block;width:100%}
.copy{font-size:10px;line-height:12.85px;text-align:justify;hyphens:auto;color:var(--ink-soft);overflow:hidden}
.copy::first-letter{font-size:26px;float:left;line-height:22px;margin-right:1px}
.more{display:inline-block;font-size:10px;text-decoration:underline;color:var(--ink-soft)}
.double-rule{height:4px;border-top:1px solid var(--ink-soft);border-bottom:1px solid var(--ink-soft)}
.headline{font:700 29px/34px "Playfair Display",Georgia,serif;text-transform:uppercase;color:var(--ink)}

.hero{left:59px;top:155px;width:458px;height:394px;background:linear-gradient(170deg,#9d9d9d 0%,#8a8a8a 45%,#5a5a5a 75%,#3d3d3d 100%)}
.hero .overlay{position:absolute;left:19px;top:147px;width:330px;color:var(--white)}
.hero h1{width:260px;font:400 29px/34px "Playfair Display",Georgia,serif;text-transform:uppercase}
.hero h2{margin-top:14px;margin-left:4px;font:700 16px/1 "Playfair Display",Georgia,serif}
.hero p{margin-top:10px;margin-left:4px;width:318px;font-size:10px;line-height:13px}
.hero .more{margin-top:12px;margin-left:4px;color:var(--white)}

.loading{position:absolute;left:0;top:1128px;width:814px;text-align:center;font-size:8.5px;color:var(--ink)}
.loading svg{vertical-align:-2px;margin-left:6px}
.footer-rule{position:absolute;left:68px;top:1155px;width:677px;border-top:2px solid #2f2525}
.footer{position:absolute;left:0;top:1173px;width:814px;text-align:center;font:400 8px/1 "Open Sans",Arial,sans-serif;color:var(--ink)}
</style>
</head>
<body>

<header class="topbar">
  <nav class="nav"><a>Products</a><a>Advertisments</a><a>About Us</a></nav>
  <div class="contact">
    <span><svg viewBox="0 0 10 8"><path d="M0 0h10v1L5 4 0 1z M0 2l5 3 5-3v6H0z"/></svg>info@trumboandkessler.example</span>
    <span><svg viewBox="0 0 10 10"><path d="M2 0l2 2-1 2c1 1 2 2 3 3l2-1 2 2-2 2C4 10 0 6 0 2z"/></svg>(02) 555 0147</span>
  </div>
</header>

<section class="masthead">
  <div class="brand">Trumbo and Kessler</div>
  <div class="rule-top"></div>
  <div class="tagline">A Puget Sound original, est. 1851</div>
  <div class="rule-double"></div>
</section>

<article class="block hero" role="img" aria-label="Grainy vintage photograph of a large passenger ferry on the water">
  <div class="overlay">
    <h1>San Fransico Pudget and Sound</h1>
    <h2>First Class Vessels:</h2>
    <p>Lorem ipsum dolor sit amet, consectetur adipisicing elit, sed do eiusmod tempor incididunt ut labore et dolore magna aliqua. Ut enim ad minim veniam, quis nostrud exercitation ullamco laboris nisi ut aliquip ex ea commodo consequat.</p>
    <a class="more">Read More »</a>
  </div>
</article>

<article class="block" style="left:535px;top:156px;width:220px">
  <p class="copy" style="height:218px">Dolor sit amet, consectetur adipisicing elit, sed do eiusmod tempor incididunt ut labore et dolore magna aliqua. Ut enim ad minim veniam, quis nostrud exercitation ullamco laboris nisi ut aliquip ex ea commodo consequat. Duis aute irure dolor in reprehenderit in voluptate velit esse cillum dolore eu fugiat nulla pariatur. Excepteur sint occaecat cupidatat non proident, sunt in culpa qui officia deserunt mollit anim id est laborum. Sed ut perspiciatis unde omnis iste natus error sit voluptatem accusantium doloremque laudantium, totam rem aperiam, eaque ipsa quae ab i proident, sunt in culpa qui officia deserunt mollit anim id est laborum. Sed ut perspiciatis unde omnis iste natus error sit voluptatem accusantium doloremque.</p>
  <a class="more" style="margin-top:12px">Learn More »</a>
  <div class="double-rule" style="margin-top:14px"></div>
</article>

<article class="block" style="left:535px;top:442px;width:222px">
  <h2 class="headline">Vintage Bike</h2>
  <div class="photo" role="img" aria-label="Black and white photo of a vintage bicycle against a white wall" style="margin-top:12px;height:158px;background:linear-gradient(180deg,#e4e4e2 0%,#d6d6d4 80%,#7a7a78 100%)"></div>
  <p class="copy" style="margin-top:28px;height:346px;width:220px">Get psum dolor sit amet, consectetur adipisicing elit, sed do eiusmod tempor incididunt ut labore et dolore magna aliqua. Ut enim ad minim veniam, quis nostrud exercitation ullamco laboris nisi ut aliquip ex ea commodo consequat. Duis aute irure dolor in reprehenderit in voluptate velit esse cillum dolore eu fugiat nulla pariatur. Excepteur sint occaecat cupidatat non proident, sunt in culpa qui officia deserunt mollit anim id est laborum. Sed ut perspiciatis unde omnis iste natus error sit voluptatem accusantium doloremque laudantium, totam rem aperiam, eaque ipsa quae ab i proident, sunt in culpa qui officia deserunt mollit anim id est laborum. Sed ut perspiciatis unde omnis iste natus error sit voluptatem accusantium doloremque laudantium, totam rem aperiam, eaque ipsa qudoloremque laudantium, totam rem aperiam, eaque ipsa quae ab i proident, sunt in culpa qui officia deserunt mollit anim id est laborum. Sed ut perspiciatis unde omnis iste natus error sit voluptatem accusantium doloremque laudantium, totam rem aperiam, eaque ipsa qudoloremque laudantium, totam rem aperiam, eaque ipsa quae ab i proident, sunt in culpa qui officia deserunt mollit anim id est laborum. Sed ut perspiciatis</p>
  <a class="more" style="margin-top:12px">Learn More »</a>
</article>

<article class="block" style="left:59px;top:575px;width:220px">
  <h2 class="headline">Ocean Steam Ships</h2>
  <div class="photo" role="img" aria-label="Black and white aerial photo of a ferry crossing dark water" style="margin-top:14px;height:157px;background:linear-gradient(160deg,#5e5e5e 0%,#4a4a4a 50%,#6a6a6a 100%)"></div>
  <p class="copy" style="margin-top:20px;height:232px">Lorem ipsum dolor sit amet, consectetur adipisicing elit, sed do eiusmod tempor incididunt ut labore et dolore magna aliqua. Ut enim ad minim veniam, quis nostrud exercitation ullamco laboris nisi ut aliquip ex ea commodo consequat. Duis aute irure dolor in reprehenderit in voluptate velit esse cillum dolore eu fugiat nulla pariatur. Excepteur sint occaecat cupidatat non proident, sunt in culpa qui officia deserunt mollit anim id est laborum. Sed ut perspiciatis unde omnis iste natus error sit voluptatem accusantium doloremque laudantium, totam rem aperiam, eaque ipsa quae ab i proident, sunt in culpa qui officia deserunt mollit anim id est laborum. Sed ut perspiciatis unde omnis iste natus error sit voluptatem accusantium doloremque laudantium, totam</p>
</article>

<article class="block" style="left:297px;top:576px;width:220px">
  <p class="copy" style="height:129px">Ipsum dolor sit amet, consectetur adipisicing elit, sed do eiusmod tempor incididunt ut labore et dolore magna aliqua. Ut enim ad minim veniam, quis nostrud exercitation ullamco laboris nisi ut aliquip ex ea commodo consequat. Duis aute irure dolor in reprehenderit in voluptate velit esse cillum dolore eu fugiat nulla pariatur. Excepteur sint occaecat cupidatat non proident, sunt in culpa qui officia deserunt.</p>
  <a class="more" style="margin-top:11px;margin-left:2px">Learn More »</a>
  <div class="double-rule" style="margin-top:24px"></div>
  <h2 class="headline" style="margin-top:15px;margin-left:2px">This House<br>is for Sale</h2>
  <div class="photo" role="img" aria-label="Black and white photo of a brick house with a curved front path" style="margin-top:14px;height:157px;background:linear-gradient(180deg,#8c8c8c 0%,#6a6a6a 40%,#4e4e4e 70%,#3e3e3e 100%)"></div>
  <p class="copy" style="margin-top:15px;height:40px">The psum dolor sit amet, consectetur adipisicing elit, sed do eiusmod tempor incididunt ut labore et dolore magna aliqua. Ut enim ad minim veniam, quis nostrud.</p>
</article>

<div class="loading">Loading more ads please wait
  <svg width="9" height="9" viewBox="0 0 10 10"><path d="M2.2 3A3.5 3.5 0 1 1 1.5 6" fill="none" stroke="var(--ink)" stroke-width="1.4"/><path d="M0.5 1v3h3z" fill="var(--ink)"/></svg>
</div>
<div class="footer-rule"></div>
<footer class="footer">Trumbo and Kessler 2018. All rights Reserved</footer>

</body>
</html>
```